Corvella Web Design Project

I am attaching my logo so I need to see applied to the website developed by you guys!!
Tbahks!!
Marcello
This is the DNA of the company
Flat and dynamic organization - Informal and respectful social approac
Innovative - Always striving for the best solution
Reliability and Quality - The value of our name
Flexibility - Ability to handle new requirements and unforeseen events
Simplicity - Technology must serve – NOT rule!
Cooperative Relations - The synergy that makes 1+1=3
We still don´t have our logo as we have another open project on artbazaar
Our company won´t be selling this equipment but providing welding services for shipyard industry, as you can see on the website below.
www.velmorix.com
Updates
Project Deadline Extended
Reason: Hi webdesigners,
I will be deciding my logo by this weekend as soon as I have decided I will post my logo to see it applied to your design!!!
Thanks
Marcello
I just Sent my logo for your attention!!!!
Industry/Entity Type
Welding
Look and feel
Each slider illustrates characteristics of the customer's brand and the style your logo design should communicate.

```html
<!DOCTYPE html>
<html lang="en">
<head>
<meta charset="utf-8">
<title>Corvella – Welding Services</title>
<link href="https://fonts.googleapis.com/css2?family=Barlow+Semi+Condensed:wght@500;600;700&family=Open+Sans:wght@400;600&display=swap" rel="stylesheet">
<style>
:root{
  --blue:#00a3e4;
  --blue-dark:#0a8fcf;
  --orange:#ff8a00;
  --orange-light:#ffb400;
  --orange-text:#f05a1a;
  --ink:#2f2f2f;
  --body:#3a3a3a;
  --muted:#8a8a8a;
  --page-bg:#ececec;
  --card:#ffffff;
  --line:#d8d8d8;
  --footer:#2b2b2b;
  --footer-bottom:#1f1f1f;
  --footer-text:#c8c8c8;
}
*{margin:0;padding:0;box-sizing:border-box}
html,body{width:979px;height:1200px;overflow:hidden}
body{background:var(--page-bg);font-family:"Open Sans",Arial,sans-serif;color:var(--body)}
.page{position:relative;width:979px;height:1200px;overflow:hidden}
.abs{position:absolute}
.head-font{font-family:"Barlow Semi Condensed","Arial Narrow",sans-serif}

/* header */
.site-header{left:0;top:0;width:979px;height:104px;background:#fff}
.brand{left:84px;top:41px;font-size:21px;font-weight:600;color:var(--ink);letter-spacing:.3px}
.social-top{left:790px;top:28px;display:flex;gap:5.5px}
.social-top span{width:22px;height:22px;border-radius:50%;background:var(--blue-dark);display:block}
.social-top span:last-child{background:#d23a2a}
.call{right:85px;top:62px;font-size:17px;color:var(--ink);font-weight:500}
.call b{color:var(--orange-text);font-weight:600}

/* nav */
.main-nav{left:0;top:104px;width:979px;height:37px;background:var(--blue);display:flex;padding-left:68px}
.main-nav a{color:#fff;text-decoration:none;font-size:13px;font-weight:600;letter-spacing:.3px;padding:0 14px;line-height:37px;border-right:1px solid rgba(255,255,255,.35)}
.main-nav a:last-child{border-right:none}

/* hero */
.hero{left:0;top:141px;width:979px;height:416px;background:linear-gradient(180deg,#7e9cc7 0%,#a9bedb 35%,#6c7788 62%,#4a4a4c 100%)}
.hero-card{left:83px;top:240px;width:261px;height:190px;background:linear-gradient(180deg,var(--orange-light),var(--orange));padding:17px 18px 0 18px;color:#fff}
.hero-card h1{font-size:21px;font-weight:600;letter-spacing:.3px;margin-bottom:6px}
.hero-card p{font-size:11.5px;line-height:18.3px;padding-left:2px}
.btn-blue{display:inline-block;margin:8px 0 0 3px;background:var(--blue);color:#fff;font-size:11.5px;padding:4px 13px;border-radius:2px}
.hero-arrows{left:852px;top:312px}

/* cards */
.card{top:523px;width:262px;height:325px;background:linear-gradient(180deg,#fff 80%,#f5f5f5);box-shadow:0 1px 2px rgba(0,0,0,.18)}
.card h2{position:absolute;left:17px;top:17px;font-size:20px;font-weight:600;color:var(--ink);letter-spacing:.2px}
.service{position:absolute;left:18px;width:230px;height:60px}
.service .thumb{position:absolute;left:0;top:0;width:88px;height:60px}
.service h3{position:absolute;left:101px;top:-2px;font-size:11.5px;font-weight:600;color:var(--blue)}
.service p{position:absolute;left:101px;top:15px;font-size:11.5px;line-height:18.3px;color:var(--body)}
.news{position:absolute;left:20px;width:220px;border-bottom:1px solid var(--line)}
.news h3{font-size:11.5px;font-weight:600;color:var(--blue);margin-bottom:2px}
.news p{font-size:11.5px;line-height:18.3px}
.news small{font-size:9.5px;color:var(--muted)}
.btn-orange{position:absolute;top:282px;width:82px;height:25px;background:var(--orange);color:#fff;font-size:11.5px;text-align:center;line-height:25px;border-radius:2px}
.video{position:absolute;left:21px;top:49px;width:218px;height:216px;background:linear-gradient(160deg,#4a5c84 0%,#5b4a3a 55%,#7a4a25 100%)}
.video-bar{position:absolute;left:0;bottom:0;width:218px;height:22px;background:#1d1d1d}

/* features */
.feature{top:864px;width:262px;height:94px;background:linear-gradient(180deg,#fff 70%,#f4f4f4);box-shadow:0 1px 2px rgba(0,0,0,.18)}
.feature h4{position:absolute;left:22px;top:29px;font-size:17px;font-weight:600;line-height:20px;color:var(--ink);letter-spacing:.3px}
.feature svg{position:absolute}

/* footer */
.site-footer{left:0;top:987px;width:979px;height:169px;background:var(--footer)}
.site-footer h5{position:absolute;font-size:13px;font-weight:600;color:#fff;letter-spacing:.3px}
.flist{position:absolute;list-style:none;font-size:10.5px;line-height:19px;color:var(--footer-text)}
.email{position:absolute;left:550px;top:43px;width:194px;height:27px;background:#e6e6e6;font-size:9.5px;color:#666;padding:7px 11px}
.signup{position:absolute;left:551px;top:80px;width:82px;height:25px;background:var(--orange-text);color:#fff;font-size:11.5px;text-align:center;line-height:25px;border-radius:2px}
.follow{position:absolute;left:786px;display:flex;align-items:center;gap:11px;font-size:10.5px;color:var(--footer-text)}
.follow span{width:32px;height:32px;border-radius:50%;background:#5d5d5d;display:block}
.legal{left:0;top:1156px;width:979px;height:44px;background:var(--footer-bottom);text-align:center;font-size:10.5px;line-height:44px;color:#8d8d8d}
</style>
</head>
<body>
<div class="page">

  <header class="site-header abs">
    <div class="brand abs head-font">LOGO HERE</div>
    <div class="social-top abs"><span></span><span></span><span></span><span></span></div>
    <div class="call abs head-font"><b>CALL NOW:</b> (555) 214 380</div>
  </header>

  <nav class="main-nav abs head-font">
    <a>HOME</a><a>ABOUT US</a><a>COMPETENCE</a><a>CASE STORY</a><a>PRODUCTS</a><a>VIDEOS</a><a>DOWNLOADS</a>
  </nav>

  <div class="hero abs" role="img" aria-label="Shipyard with a crane lifting a large steel hull section"></div>
  <div class="hero-card abs">
    <h1 class="head-font">WELDING SERVICES</h1>
    <p>Lorem Ipsum is simply dummy text of the printing and typesetting industry. Lorem Ipsum has been the industry's standard dummy text ever since the 1500s, when an unknown printer.</p>
    <span class="btn-blue">Read More</span>
  </div>
  <svg class="hero-arrows abs" width="40" height="32" viewBox="0 0 40 32" fill="none" stroke="#fff" stroke-width="1.6">
    <path d="M14 3 L2 16 L14 29"/><path d="M26 3 L38 16 L26 29"/>
  </svg>

  <section class="card abs" style="left:83px">
    <h2 class="head-font">OUR SERVICES</h2>
    <div class="service" style="top:46px"><div class="thumb" role="img" aria-label="Welder at work with sparks" style="background:linear-gradient(135deg,#3a3a3a,#b5502a 60%,#d8a040)"></div><h3>Welding Design</h3><p>Lorem Ipsum is simply dummy text of printing</p></div>
    <div class="service" style="top:113px"><div class="thumb" role="img" aria-label="Welding tools on a steel floor" style="background:linear-gradient(135deg,#7d7a72,#5a5650 60%,#9a9590)"></div><h3>Welding Coordination</h3><p>Lorem Ipsum is simply dummy text of printing</p></div>
    <div class="service" style="top:180px"><div class="thumb" role="img" aria-label="Workers at a shipyard welding station" style="background:linear-gradient(180deg,#9eb0c8,#5e6066 50%,#45474a)"></div><h3>Welder Qualification</h3><p>Lorem Ipsum is simply dummy text of printing</p></div>
    <div class="service" style="top:247px"><div class="thumb" role="img" aria-label="Welder kneeling on a steel plate" style="background:linear-gradient(135deg,#8a7a3a,#4d5a3a 55%,#7a8ab8)"></div><h3>Welding Procedure</h3><p>Lorem Ipsum is simply dummy text of printing</p></div>
  </section>

  <section class="card abs" style="left:358px">
    <h2 class="head-font">NEWS AND UPDATES</h2>
    <div class="news" style="top:50px;height:77px"><h3>Lorem Ipsum is simply dummy</h3><p>Lorem Ipsum is simply dummy text of the printing and typesetting industry. Lorem Ipsum has been industry's <small>12 / 05 / 2014</small></p></div>
    <div class="news" style="top:134px;height:78px"><h3>Lorem Ipsum is simply dummy</h3><p>Lorem Ipsum is simply dummy text of the printing and typesetting industry. Lorem Ipsum has been industry's <small>12 / 05 / 2014</small></p></div>
    <div class="news" style="top:218px;border:none"><h3>Lorem Ipsum is simply dummy</h3><p>Lorem Ipsum is simply dummy text of the printing and typesetting.<small>12 / 05 / 2014</small></p></div>
    <div class="btn-orange" style="left:19px">Show All</div>
  </section>

  <section class="card abs" style="left:633px">
    <h2 class="head-font" style="left:21px">VIDEOS</h2>
    <div class="video" role="img" aria-label="Video still of a worker cutting steel with a torch">
      <svg style="position:absolute;left:84px;top:92px" width="46" height="36" viewBox="0 0 46 36"><rect width="46" height="36" rx="8" fill="rgba(255,255,255,.35)"/><path d="M18 9 L31 18 L18 27Z" fill="#333"/></svg>
      <div class="video-bar">
        <svg style="position:absolute;left:0;top:0" width="30" height="22"><rect width="30" height="22" fill="var(--blue)"/><path d="M12 6 L20 11 L12 16Z" fill="#fff"/></svg>
        <div style="position:absolute;left:42px;top:7px;width:135px;height:7px;background:#fff"><div style="width:38px;height:7px;background:#aaa"></div></div>
        <svg style="position:absolute;right:0;top:-3px" width="30" height="25"><rect width="30" height="25" fill="var(--blue)"/><rect x="9" y="7" width="9" height="7" fill="none" stroke="#fff" stroke-width="1.3"/><rect x="13" y="11" width="9" height="7" fill="none" stroke="#fff" stroke-width="1.3"/></svg>
      </div>
    </div>
    <div class="btn-orange" style="left:22px">Show All</div>
  </section>

  <div class="feature abs" style="left:83px">
    <h4 class="head-font">ASK THE<br>EXPERTS</h4>
    <svg style="left:193px;top:22px" width="48" height="50" viewBox="0 0 48 50" fill="#6a6a6a"><circle cx="24" cy="13" r="11"/><path d="M2 50 C2 34 10 28 24 28 C38 28 46 34 46 50Z"/><path d="M22 30 L26 30 L27 44 L24 48 L21 44Z" fill="#fff"/></svg>
  </div>
  <div class="feature abs" style="left:358px">
    <h4 class="head-font" style="left:24px">INFO<br>CENTER</h4>
    <div class="head-font" style="position:absolute;left:199px;top:8px;font-size:66px;font-weight:700;color:#6a6a6a;line-height:70px">?</div>
  </div>
  <div class="feature abs" style="left:633px">
    <h4 class="head-font" style="left:22px">SHIPYARD<br>INDUSTRY</h4>
    <svg style="left:183px;top:28px" width="60" height="36" viewBox="0 0 60 36" fill="#6a6a6a"><path d="M0 20 L60 16 C56 28 48 34 38 34 L10 34 C5 30 2 25 0 20Z"/><path d="M14 17 L18 6 L44 4 L50 15Z"/><rect x="24" y="0" width="8" height="6"/></svg>
  </div>

  <footer class="site-footer abs">
    <h5 class="head-font" style="left:83px;top:17px">ABOUT US</h5>
    <ul class="flist" style="left:83px;top:40px"><li>Home</li><li>About Us</li><li>Competence</li><li>Case Story</li><li>Products</li><li>Videos</li></ul>
    <ul class="flist" style="left:230px;top:40px"><li>Welding design</li><li>Welding coordination</li><li>Welder qualification</li><li>Welding procedure</li><li>specification</li></ul>
    <ul class="flist" style="left:413px;top:40px"><li>Shipyard industry</li><li>Engine rooms</li><li>Plumbing</li><li>AC rooms</li><li>Maintenance</li></ul>
    <h5 class="head-font" style="left:549px;top:17px">NEWSLETTER SIGNUP</h5>
    <div class="email">Email Address</div>
    <div class="signup">Sign up</div>
    <h5 class="head-font" style="left:787px;top:17px">FOLLOW US</h5>
    <div class="follow" style="top:39px"><span></span>Friendwall</div>
    <div class="follow" style="top:76px"><span></span>Chirpline</div>
    <div class="follow" style="top:112px"><span></span>ClipStream</div>
  </footer>
  <div class="legal abs">Terms Of Use &nbsp;|&nbsp; Privacy Statement &nbsp;|&nbsp; © 2014. Corvella .All Rights Reserved</div>

</div>
</body>
</html>
```